Anzeigengestaltung für ambulanten Pflegedienst
Zielgruppe
Ambulanter Pflegedienst
Aufgabenstellung
Die Maße und an die Grafik anbei orientieren. Es muss bitte auffallen. Keine Stockfotos Telefonummer und Name sowie Ambulanter Pflegedienst muss auf der Anzeige stehen wie Grafik Anbei.

```html
<!DOCTYPE html>
<html lang="de">
<head>
<meta charset="utf-8">
<title>Anzeige Ambulanter Pflegedienst</title>
<link rel="stylesheet" href="https://fonts.googleapis.com/css2?family=Open+Sans:wght@400;600;800&display=swap">
<style>
  :root {
    --page-bg: #e9e8e6;
    --purple-deep: #3f1f55;
    --purple-main: #6a2a8e;
    --purple-band: #65278a;
    --purple-soft: #9a6ab8;
    --lavender: #f6f1f9;
    --lavender-mid: #e7d9ef;
    --white: #ffffff;
    --logo-text: #6e6660;
  }
  html, body {
    margin: 0;
    width: 1200px;
    height: 1200px;
    overflow: hidden;
    background: var(--page-bg);
  }
  .canvas {
    width: 1200px;
    height: 1200px;
    display: flex;
    align-items: center;
    justify-content: center;
  }
  .ad {
    display: block;
    width: 1120px;
    height: 789px;
    box-shadow: 0 0 0 1px #8d8d8d;
  }
  .headline {
    font-family: "Open Sans", sans-serif;
    font-weight: 800;
    font-size: 35px;
    fill: var(--white);
  }
  .contact-text {
    font-family: "Open Sans", sans-serif;
    font-weight: 400;
    font-size: 21px;
    fill: var(--white);
  }
  .brand-name {
    font-family: "Open Sans", sans-serif;
    font-weight: 600;
    font-size: 13px;
    letter-spacing: 0.5px;
    fill: var(--logo-text);
  }
  .icon-line {
    fill: none;
    stroke: var(--white);
    stroke-width: 1.8;
  }
</style>
</head>
<body>
<main class="canvas">
  <svg class="ad" viewBox="0 0 620 437" xmlns="http://www.w3.org/2000/svg">
    <defs>
      <linearGradient id="heroGradient" x1="0" y1="0" x2="1" y2="0">
        <stop offset="0" stop-color="#6d2b92"/>
        <stop offset="1" stop-color="#3b1d4f"/>
      </linearGradient>
      <linearGradient id="accentGradient" x1="0" y1="0" x2="1" y2="1">
        <stop offset="0" stop-color="#8c55ad"/>
        <stop offset="1" stop-color="#b391c9"/>
      </linearGradient>
      <linearGradient id="patternGradient" x1="0" y1="0" x2="1" y2="1">
        <stop offset="0" stop-color="var(--lavender)"/>
        <stop offset="1" stop-color="var(--lavender-mid)"/>
      </linearGradient>
      <clipPath id="adClip"><rect width="620" height="437"/></clipPath>
    </defs>

    <g clip-path="url(#adClip)">
      <rect class="pattern-field" width="620" height="437" fill="url(#patternGradient)" role="img" aria-label="Muster aus Pflege-Symbolen: Herz in Händen, Haus mit Herz, betreute Personen"/>

      <circle class="hero-circle" cx="190" cy="90" r="205" fill="url(#heroGradient)"/>

      <rect class="contact-band" x="0" y="335" width="620" height="102" fill="var(--purple-band)"/>

      <circle class="accent-circle" cx="528" cy="355" r="142" fill="url(#accentGradient)"/>
      <circle class="brand-disc" cx="540" cy="382" r="80" fill="var(--white)"/>
    </g>

    <g class="headline-block">
      <text class="headline" x="24" y="93">AMBULANTER</text>
      <text class="headline" x="24" y="136">PFLEGEDIENST</text>
      <text class="headline" x="24" y="180">in Berlin-Rudow</text>
    </g>

    <g class="contact-phone">
      <circle class="icon-line" cx="44" cy="366" r="15"/>
      <path class="icon-line" d="M37 358 c2-2 4-2 5 0 l2 4 c0 2-2 2-2 4 c1 3 3 5 6 6 c2 0 2-2 4-2 l4 2 c2 1 2 3 0 5 c-3 3-7 2-11-1 c-5-4-8-8-9-12 c-1-3 0-5 1-6z"/>
      <text class="contact-text" x="73" y="374">+49 (0)30 555014700</text>
    </g>

    <g class="contact-web">
      <circle class="icon-line" cx="44" cy="407" r="15"/>
      <ellipse class="icon-line" cx="44" cy="407" rx="6.5" ry="15"/>
      <line class="icon-line" x1="29" y1="407" x2="59" y2="407"/>
      <path class="icon-line" d="M32 399 h24 M32 415 h24"/>
      <text class="contact-text" x="72" y="415">pflegeteam-linde.de</text>
    </g>

    <g class="brand">
      <circle cx="540" cy="358" r="5" fill="var(--purple-main)"/>
      <text class="brand-name" x="540" y="396" text-anchor="middle">PFLEGETEAM LINDE</text>
    </g>
  </svg>
</main>
</body>
</html>
```